product leaflet for the aviation industry

Hello,
please prepare a leaflet design in A4 format, double-sided. Technical data can be found in the "A4 - leaflet" file on the first page. The leaflet can be arranged freely, but please include all substantive content from the "A4 - leaflet" file (pages 2 and 3). The company logo can be found in the attachment. Some of the photos can be downloaded from: https://vendrimax.qpanel.pl/.
The company operates for the aviation industry, so there may be an airplane or an aircraft turbine in the background.
Thank you in advance!
Target Market(s)
factories producing aircraft turbines
Industry/Entity Type
air

```html
<!DOCTYPE html>
<html lang="en">
<head>
<meta charset="utf-8">
<title>Vendrimax – Technical Consumables for Aerospace leaflet</title>
<link rel="stylesheet" href="https://fonts.googleapis.com/css2?family=Bebas+Neue&family=Roboto:ital,wght@0,400;0,500;0,700;1,400;1,500&display=swap">
<style>
:root{
  --bg:#2c2c2c;
  --paper:#ffffff;
  --royal:#2f4ea3;
  --royal-dark:#243f8c;
  --sky:#1b87d1;
  --orange:#f5a524;
  --ink:#1d2a55;
  --grey:#5d6270;
  --line:#6a7cc8;
  --thumb:#eef0f4;
  --footer:#0d0d10;
}
*{box-sizing:border-box;margin:0;padding:0}
html,body{width:1200px;height:1200px;overflow:hidden;background:var(--bg)}
body{position:relative;font-family:"Roboto",Arial,sans-serif;color:var(--grey)}
.page{position:absolute;top:192px;width:542px;height:761px;background:var(--paper);overflow:hidden}
.page--front{left:45px}
.page--back{left:614px}
.shapes{position:absolute;left:0;top:0;width:542px;height:761px}
.abs{position:absolute}
.display{font-family:"Bebas Neue",Impact,sans-serif;font-weight:400;letter-spacing:.2px}

/* front header */
.brand{position:absolute;left:46px;top:80px;width:180px;display:flex;align-items:center;gap:8px}
.brand__square{width:14px;height:14px;background:var(--royal)}
.brand__name{font-family:"Roboto",Arial,sans-serif;font-weight:700;font-size:22px;color:var(--royal);letter-spacing:.5px}
.hero-title{position:absolute;right:44px;top:25px;text-align:right;color:#fff;font-size:31px;line-height:27px}
.intro{position:absolute;left:17px;top:132px;width:208px;color:#fff;font-size:9.6px;line-height:11.8px}
.intro p+p{margin-top:11px}
.section-title{position:absolute;color:#fff;font-size:26px;line-height:31px;white-space:nowrap}
.section-title--back{font-size:20.5px;letter-spacing:0}

/* cards */
.card{position:absolute;border:1px solid var(--line);border-radius:4px;background:#fff;padding:5px 7px 4px 26px}
.card__title{color:var(--royal);font-size:9.6px;line-height:11.5px;font-weight:500;margin-bottom:3px}
.card__text{font-size:6.4px;line-height:8.2px;text-align:justify;color:var(--grey)}
.thumb{position:absolute;width:60px;height:60px;border-radius:50%;border:2px solid var(--orange);background:#fff;padding:4px}
.thumb__fill{width:100%;height:100%;border-radius:50%;background:radial-gradient(circle at 40% 40%,#ffffff,#cfd3db)}

/* footer */
.footer{position:absolute;left:0;top:711px;width:542px;height:50px;background:var(--footer);color:#fff}
.footer__brand{position:absolute;left:18px;top:16px;display:flex;align-items:center;gap:6px}
.footer__square{width:12px;height:12px;background:var(--royal)}
.footer__name{font-weight:700;font-size:16px;color:#8fa2e0;letter-spacing:.5px}
.footer__contact{position:absolute;left:170px;top:6px;font-size:8.3px;line-height:10.4px}
.footer__address{position:absolute;left:280px;top:17px;font-size:8.3px;line-height:10.4px}
.footer__web{position:absolute;left:433px;top:19px;font-size:10.5px;font-weight:500}
.footer__icon{display:inline-block;vertical-align:-1px;margin-right:3px}
.footer__label{font-weight:500}

/* back page */
.services-label{position:absolute;left:291px;top:315px;color:var(--royal);font-size:25px}
.services-sub{position:absolute;left:396px;top:318px;color:#fff;font-size:19px}
.services-copy{position:absolute;left:255px;top:353px;width:262px;color:#fff;font-size:9.6px;line-height:11.8px;text-align:justify}
.customers-label{position:absolute;left:437px;top:414px;color:#fff;font-size:21px}
.customers-lead{position:absolute;left:34px;top:447px;font-size:8.6px;font-style:italic;color:var(--royal);font-weight:500}
.partner{position:absolute;width:90px;height:26px;border:1px solid #e0e2e8;border-radius:3px;background:#fff;display:flex;align-items:center;justify-content:center}
.partner__mark{width:46px;height:10px;border-radius:2px;background:#c9cfdd}
.questions-label{position:absolute;left:412px;top:539px;color:#fff;font-size:12.5px;font-weight:500}
.contact-card{position:absolute;left:331px;top:573px;width:185px;height:97px;background:#fff;border-radius:8px;text-align:center;color:#111}
.contact-card__name{font-size:20px;color:var(--royal);margin-top:8px}
.contact-card__role{font-size:12.5px;margin-top:1px}
.contact-card__line{font-size:10px;line-height:12.5px}
.contact-card__phone{margin-top:13px}
.where-label{position:absolute;left:25px;top:688px;color:#fff;font-size:12.5px;font-weight:500}
.where-copy{position:absolute;left:176px;top:683px;width:345px;color:#fff;font-size:8.2px;line-height:10px;text-align:center}
.where-copy b{color:var(--orange);font-weight:500}
</style>
</head>
<body>

<!-- FRONT PAGE -->
<section class="page page--front" aria-label="Leaflet front page">
  <svg class="shapes" viewBox="0 0 542 761">
    <defs>
      <linearGradient id="sky-photo" x1="0" y1="0" x2="0" y2="1">
        <stop offset="0" stop-color="#5e7aa8"/>
        <stop offset=".45" stop-color="#e6a25a"/>
        <stop offset=".7" stop-color="#9a8a7e"/>
        <stop offset="1" stop-color="#3b3f4a"/>
      </linearGradient>
    </defs>
    <polygon points="292,0 301,0 276,116 267,116" fill="var(--royal)"/>
    <polygon points="306,0 542,0 542,116 281,116" fill="var(--orange)"/>
    <rect x="0" y="118" width="290" height="182" fill="var(--royal)"/>
    <polygon points="262,118 542,118 542,300 226,300" fill="url(#sky-photo)" role="img" aria-label="Photo of a business jet and its turbofan engine on the apron at sunset"/>
    <polygon points="0,305 374,305 364,336 0,336" fill="var(--sky)"/>
    <polygon points="377,305 386,305 376,336 367,336" fill="var(--orange)"/>
  </svg>

  <div class="brand"><span class="brand__square"></span><span class="brand__name">VENDRIMAX</span></div>
  <h1 class="hero-title display">Technical<br>Consumables<br>for Aerospace</h1>

  <div class="intro">
    <p>Vendrimax specializes in manufacturing, spare parts details &amp; consumable materials used in special processes such as thermal spraying, hardfacing, brazing, welding, chemical processing, and more. We also produce tooling for testing aerospace materials and coatings.</p>
    <p>Our primary customers include manufacturers of new engine components &amp; maintenance, repair, and overhaul (MRO) facilities worldwide. Our production facility is AS9100 certified, and we hold a military license.</p>
  </div>

  <h2 class="section-title display" style="left:35px;top:306px">Consumables for Special Processes</h2>

  <div class="card" style="left:64px;top:345px;width:196px;height:83px">
    <h3 class="card__title">Coupons &amp; Substrates Machining</h3>
    <p class="card__text">We specialize in manufacturing high-quality test coupons, substrates, specimens, samples, buttons, panels, discs, and strips for thermal spray, cold spray, chemical processing &amp; welding applications in the aviation industry. Our range of materials includes nickel and cobalt-based superalloys, titanium, hardened steel, and single crystals.</p>
  </div>
  <div class="thumb" style="left:22px;top:357px"><div class="thumb__fill" role="img" aria-label="Metal test coupons and discs"></div></div>

  <div class="card" style="left:64px;top:435px;width:196px;height:86px">
    <h3 class="card__title">Reusable Silicone Masking<br>/Hard Masking</h3>
    <p class="card__text">Vendrimax's reusable silicone masking improves productivity and reduces costs by providing precise, durable protection for aero and gas turbine engine parts during processes such as thermal spray, grit blasting, shot peening, chemical processing, and vibratory finishing.</p>
  </div>
  <div class="thumb" style="left:22px;top:448px"><div class="thumb__fill" role="img" aria-label="Green silicone masking ring"></div></div>

  <div class="card" style="left:64px;top:528px;width:196px;height:83px">
    <h3 class="card__title">Fan Blade Leading Edge Patches,<br>Custom Spare Metal Parts</h3>
    <p class="card__text">Manufacturer of aerospace components and spare parts for turbine engines, offering a wide range of materials.</p>
  </div>
  <div class="thumb" style="left:22px;top:540px"><div class="thumb__fill" role="img" aria-label="Fan blade leading edge patches"></div></div>

  <div class="card" style="left:64px;top:618px;width:196px;height:85px">
    <h3 class="card__title">Honeycomb Tack Welding Shims</h3>
    <p class="card__text">Our shims are precision-made with flat surfaces, eliminating issues like convex edges that cause scorching on contact points and honeycomb surfaces. They ensure reliable performance and solve problems related to improper shim contact in demanding applications.</p>
  </div>
  <div class="thumb" style="left:22px;top:631px"><div class="thumb__fill" role="img" aria-label="Tack welding shims"></div></div>

  <div class="card" style="left:318px;top:345px;width:197px;height:83px">
    <h3 class="card__title">Coupons regeneration</h3>
    <p class="card__text">Our regeneration service restores coated coupons to their original specifications. By using mechanical stripping processes, we offer a faster and more cost-effective alternative to producing new coupons. This results in significant savings on raw materials and heat treatment, while also reducing waste.</p>
  </div>
  <div class="thumb" style="left:278px;top:355px"><div class="thumb__fill" role="img" aria-label="Coated coupon before and after regeneration"></div></div>

  <div class="card" style="left:318px;top:435px;width:197px;height:86px">
    <h3 class="card__title">Pre-Sintered Diffusion<br>Brazing Preforms (PSP)</h3>
    <p class="card__text">Superalloy and brazing products for aero engines, ideal for high-temperature repairs and dimensional restoration, with low porosity and minimal shrinkage.</p>
  </div>
  <div class="thumb" style="left:278px;top:448px"><div class="thumb__fill" role="img" aria-label="Pre-sintered brazing preform"></div></div>

  <div class="card" style="left:318px;top:528px;width:197px;height:83px">
    <h3 class="card__title">Honeycomb</h3>
    <p class="card__text">Honeycomb structures, with or without embedded brazing material, tailored to customer specifications and available in various forms like segments and rings, offer reduced assembly time with tape application, while Vendrimax also provides additional surface treatments as a value-added service.</p>
  </div>
  <div class="thumb" style="left:278px;top:540px"><div class="thumb__fill" role="img" aria-label="Metal honeycomb structure"></div></div>

  <div class="card" style="left:318px;top:618px;width:197px;height:85px">
    <h3 class="card__title">Custom Feeler Gauges<br>Manufacturing</h3>
    <p class="card__text">Thanks to our WEDM capabilities, we manufacture precise tooling for measuring thickness, gaps, and spacing, such as the 0.1 mm feeler gauge set.</p>
  </div>
  <div class="thumb" style="left:278px;top:631px"><div class="thumb__fill" role="img" aria-label="Fan of feeler gauge blades"></div></div>

  <footer class="footer">
    <svg class="abs" style="left:0;top:0" width="542" height="50" aria-hidden="true">
      <polygon points="418,0 542,0 542,50 405,50" fill="var(--royal)"/>
      <polygon points="407,0 414,0 401,50 394,50" fill="var(--sky)"/>
    </svg>
    <div class="footer__brand"><span class="footer__square"></span><span class="footer__name">VENDRIMAX</span></div>
    <div class="footer__contact">
      <div class="footer__label">INTERNATIONAL LINE</div>
      <div><svg class="footer__icon" width="7" height="7" viewBox="0 0 10 10"><path d="M2 0l2 2.5-1 1.2c.6 1.3 1.6 2.3 2.9 2.9l1.2-1L10 7.7 8.6 10C4 9.5.5 6 0 1.4z" fill="var(--orange)"/></svg>+48 500 214 386</div>
      <div><svg class="footer__icon" width="7" height="6" viewBox="0 0 10 8"><rect width="10" height="8" rx="1" fill="var(--orange)"/><path d="M0 1l5 3.5L10 1" stroke="#000" fill="none"/></svg>info@vendrimax.com</div>
    </div>
    <div class="footer__address">
      <div><svg class="footer__icon" width="6" height="8" viewBox="0 0 10 14"><path d="M5 0a5 5 0 0 1 5 5c0 4-5 9-5 9S0 9 0 5a5 5 0 0 1 5-5z" fill="var(--orange)"/><circle cx="5" cy="5" r="2" fill="#000"/></svg>12 Hangarowa Street</div>
      <div>05-410 Nowy Lot, Poland</div>
    </div>
    <div class="footer__web"><svg class="footer__icon" width="11" height="11" viewBox="0 0 12 12"><circle cx="6" cy="6" r="5.3" fill="none" stroke="#fff"/><ellipse cx="6" cy="6" rx="2.3" ry="5.3" fill="none" stroke="#fff"/><path d="M.7 6h10.6" stroke="#fff"/></svg> VENDRIMAX.COM</div>
  </footer>
</section>

<!-- BACK PAGE -->
<section class="page page--back" aria-label="Leaflet back page">
  <svg class="shapes" viewBox="0 0 542 761">
    <defs>
      <linearGradient id="machine-photo" x1="0" y1="0" x2="1" y2="1">
        <stop offset="0" stop-color="#e9ecef"/>
        <stop offset=".6" stop-color="#c9ced4"/>
        <stop offset="1" stop-color="#8e959e"/>
      </linearGradient>
      <linearGradient id="map-fill" x1="0" y1="0" x2="1" y2="0">
        <stop offset="0" stop-color="#2a8fd6"/>
        <stop offset="1" stop-color="#1b7cc4"/>
      </linearGradient>
    </defs>
    <polygon points="0,8 230,8 221,41 0,41" fill="var(--royal)"/>
    <polygon points="234,8 243,8 234,41 225,41" fill="var(--orange)"/>
    <polygon points="0,146 272,146 263,178 0,178" fill="var(--royal)"/>
    <polygon points="276,146 285,146 276,178 267,178" fill="var(--orange)"/>

    <polygon points="0,293 205,293 242,425 0,425" fill="var(--orange)"/>
    <polygon points="0,295 200,295 232,425 0,425" fill="url(#machine-photo)" role="img" aria-label="Row of wire EDM machines on a workshop floor"/>
    <polygon points="384,316 542,316 542,341 377,341" fill="var(--orange)"/>
    <polygon points="230,343 542,343 542,398 244,398" fill="var(--royal)"/>
    <polygon points="424,412 542,412 542,441 417,441" fill="var(--orange)"/>

    <rect x="22" y="538" width="250" height="140" rx="10" fill="url(#map-fill)" opacity=".95" role="img" aria-label="World map with office and customer locations marked"/>
    <polygon points="402,537 542,537 542,560 396,560" fill="var(--sky)"/>
    <polygon points="318,560 542,560 542,683 290,683" fill="var(--royal)"/>
    <polygon points="0,683 158,683 150,711 0,711" fill="var(--royal)"/>
    <polygon points="162,679 542,679 542,711 154,711" fill="var(--royal-dark)"/>
    <polygon points="154,681 161,681 152,711 145,711" fill="var(--sky)"/>
  </svg>

  <h2 class="section-title section-title--back display" style="left:18px;top:10px">Modern Aviation Materials</h2>

  <div class="card" style="left:64px;top:50px;width:197px;height:86px">
    <h3 class="card__title">Ceramic Composites<br>(Sic-SiC CMC)</h3>
    <p class="card__text">Vendrimax supplies CMC SiC-SiC materials and components for aerospace and R&amp;D, driven by the growing use of CMCs in high-temperature engine parts.</p>
  </div>
  <div class="thumb" style="left:22px;top:64px"><div class="thumb__fill" role="img" aria-label="Ceramic composite blocks"></div></div>

  <div class="card" style="left:312px;top:50px;width:204px;height:86px">
    <h3 class="card__title">Aerospace Nickel &amp; Cobalt Base Superalloys, Titanium, Steel, Aluminium Alloys</h3>
    <p class="card__text">Vendrimax offers a comprehensive range of aerospace raw materials (wrought and cast), including nickel, cobalt and single-crystal grades and many others. We are also able to supply difficult to find raw materials in required shapes and dimensions.</p>
  </div>
  <div class="thumb" style="left:270px;top:64px"><div class="thumb__fill" role="img" aria-label="Stacked metal alloy sheets"></div></div>

  <h2 class="section-title section-title--back display" style="left:20px;top:147px">Consumables for Aerospace Labs</h2>

  <div class="card" style="left:64px;top:185px;width:197px;height:86px">
    <h3 class="card__title">High-temperature Custom<br>Metal Accessories</h3>
    <p class="card__text">Custom accessories and high-temperature equipment such as pull rods, couplings, fixtures, made of cast nickel superalloys, for creep, stress rupture and tensile testing at elevated temperatures up to 1300°C.</p>
  </div>
  <div class="thumb" style="left:22px;top:200px"><div class="thumb__fill" role="img" aria-label="Metal test couplings"></div></div>

  <div class="card" style="left:312px;top:185px;width:204px;height:86px">
    <h3 class="card__title">Coating Evaluation Laboratory<br>Accessories</h3>
    <p class="card__text">Manufacturing of custom laboratory accessories including, Gravity or pressure type V-grooved curing fixture for Tensile Bond Strength test of coating, Loading fixtures, concentricity gauge with dial indicator and more...</p>
  </div>
  <div class="thumb" style="left:270px;top:200px"><div class="thumb__fill" role="img" aria-label="V-grooved curing fixture"></div></div>

  <h2 class="services-label display">Services</h2>
  <h3 class="services-sub display">Wire EDM (WEDM)</h3>
  <p class="services-copy">Our advanced WEDM technology allows cutting materials up to 700 mm thick, ensuring minimal thermal impact and the highest precision.</p>

  <h2 class="customers-label display">Customers</h2>
  <p class="customers-lead">Our experience &amp; commitment to quality has been recognized by leading aircraft engine manufacturers such as:</p>

  <div class="partner" style="left:26px;top:468px"><span class="partner__mark"></span></div>
  <div class="partner" style="left:126px;top:468px"><span class="partner__mark"></span></div>
  <div class="partner" style="left:226px;top:468px"><span class="partner__mark"></span></div>
  <div class="partner" style="left:326px;top:468px"><span class="partner__mark"></span></div>
  <div class="partner" style="left:426px;top:468px"><span class="partner__mark"></span></div>
  <div class="partner" style="left:26px;top:498px"><span class="partner__mark"></span></div>
  <div class="partner" style="left:126px;top:498px"><span class="partner__mark"></span></div>
  <div class="partner" style="left:226px;top:498px"><span class="partner__mark"></span></div>
  <div class="partner" style="left:326px;top:498px"><span class="partner__mark"></span></div>
  <div class="partner" style="left:426px;top:498px"><span class="partner__mark"></span></div>

  <p class="questions-label">ANY QUESTIONS?</p>
  <div class="contact-card">
    <p class="contact-card__name">Maren Kowal</p>
    <p class="contact-card__role">Sales Director</p>
    <p class="contact-card__line contact-card__phone">+44 (0) 7700 90 04 12</p>
    <p class="contact-card__line">maren.kowal@vendrimax.com</p>
  </div>

  <p class="where-label">WHERE ARE WE?</p>
  <p class="where-copy">We're available across 6 continents. Contact our Sales Director or reach us directly at <b>info@vendrimax.com</b>, and our headquarters will promptly handle your inquiry!</p>

  <footer class="footer">
    <svg class="abs" style="left:0;top:0" width="542" height="50" aria-hidden="true">
      <polygon points="418,0 542,0 542,50 405,50" fill="var(--royal)"/>
      <polygon points="407,0 414,0 401,50 394,50" fill="var(--sky)"/>
    </svg>
    <div class="footer__brand"><span class="footer__square"></span><span class="footer__name">VENDRIMAX</span></div>
    <div class="footer__contact">
      <div class="footer__label">INTERNATIONAL LINE</div>
      <div><svg class="footer__icon" width="7" height="7" viewBox="0 0 10 10"><path d="M2 0l2 2.5-1 1.2c.6 1.3 1.6 2.3 2.9 2.9l1.2-1L10 7.7 8.6 10C4 9.5.5 6 0 1.4z" fill="var(--orange)"/></svg>+48 500 214 386</div>
      <div><svg class="footer__icon" width="7" height="6" viewBox="0 0 10 8"><rect width="10" height="8" rx="1" fill="var(--orange)"/><path d="M0 1l5 3.5L10 1" stroke="#000" fill="none"/></svg>info@vendrimax.com</div>
    </div>
    <div class="footer__address">
      <div><svg class="footer__icon" width="6" height="8" viewBox="0 0 10 14"><path d="M5 0a5 5 0 0 1 5 5c0 4-5 9-5 9S0 9 0 5a5 5 0 0 1 5-5z" fill="var(--orange)"/><circle cx="5" cy="5" r="2" fill="#000"/></svg>12 Hangarowa Street</div>
      <div>05-410 Nowy Lot, Poland</div>
    </div>
    <div class="footer__web"><svg class="footer__icon" width="11" height="11" viewBox="0 0 12 12"><circle cx="6" cy="6" r="5.3" fill="none" stroke="#fff"/><ellipse cx="6" cy="6" rx="2.3" ry="5.3" fill="none" stroke="#fff"/><path d="M.7 6h10.6" stroke="#fff"/></svg> VENDRIMAX.COM</div>
  </footer>
</section>

</body>
</html>
```